Letterhead for Dorian Welk

I need a letterhead based on the business card design

Industry/Entity Type

Business

Requirements
Must have
• Footer: Dorian Welk Naturopath
Shop 4123c, 46 Carrow Lane, Sydney 2000

```html
<!DOCTYPE html>
<html lang="en">
<head>
<meta charset="utf-8">
<title>Dorian Welk Naturopathy – Letterhead</title>
<link href="https://fonts.googleapis.com/css2?family=Montserrat:wght@500;600&family=Questrial&display=swap" rel="stylesheet">
<style>
  :root {
    --orange: #f2921f;
    --orange-soft: #f7c58a;
    --leaf-tint: #f9dcb8;
    --leaf-tint-light: #fdf1e3;
    --paper: #ffffff;
    --white: #ffffff;
  }
  * { margin: 0; padding: 0; box-sizing: border-box; }
  html, body {
    width: 857px;
    height: 1200px;
    overflow: hidden;
    background: var(--paper);
  }
  .letterhead {
    position: relative;
    width: 857px;
    height: 1200px;
    background: var(--paper);
    overflow: hidden;
    font-family: "Questrial", "Century Gothic", sans-serif;
  }
  .header-shape {
    position: absolute;
    top: 0;
    left: 0;
    width: 857px;
    height: 760px;
  }
  .brand-mark {
    position: absolute;
    top: 38px;
    left: 70px;
    width: 115px;
    height: 115px;
    border-radius: 50%;
    background: rgba(255, 255, 255, 0.35);
  }
  .brand {
    position: absolute;
    top: 58px;
    left: 235px;
    width: 450px;
    text-align: center;
    color: var(--white);
  }
  .brand-name {
    font-family: "Montserrat", "Century Gothic", sans-serif;
    font-weight: 600;
    font-size: 46px;
    letter-spacing: 2px;
    line-height: 1;
    white-space: nowrap;
  }
  .brand-rule {
    height: 2px;
    background: var(--white);
    margin: 9px 0 5px;
  }
  .brand-tagline {
    font-size: 17px;
    letter-spacing: 8px;
    line-height: 1;
    white-space: nowrap;
  }
  .brand-contact {
    margin-top: 7px;
    font-size: 10px;
    letter-spacing: 0.5px;
    line-height: 1;
    text-align: left;
    white-space: nowrap;
  }
  .leaf-decoration {
    position: absolute;
    top: 300px;
    left: 530px;
    width: 327px;
    height: 840px;
    background: radial-gradient(ellipse at 70% 45%, var(--leaf-tint) 0%, var(--leaf-tint-light) 55%, rgba(255,255,255,0) 75%);
    border-radius: 60% 0 0 40%;
  }
  .footer {
    position: absolute;
    left: 0;
    bottom: 0;
    width: 857px;
    height: 44px;
    background: var(--orange);
    color: var(--white);
    font-size: 12px;
    letter-spacing: 0.5px;
    display: flex;
    align-items: center;
    justify-content: center;
  }
  .footer-band-light {
    position: absolute;
    left: 0;
    bottom: 44px;
    width: 857px;
    height: 4px;
    background: var(--orange-soft);
  }
</style>
</head>
<body>
  <main class="letterhead">
    <svg class="header-shape" viewBox="0 0 857 760" aria-hidden="true">
      <path d="M0 0 H857 V215 C600 220 260 260 110 540 C70 610 30 680 0 740 Z" fill="var(--orange-soft)"/>
      <path d="M0 0 H857 V195 C600 198 250 235 95 510 C60 575 25 640 0 700 Z" fill="var(--orange)"/>
    </svg>

    <div class="brand-mark" aria-hidden="true"></div>

    <header class="brand">
      <h1 class="brand-name">DORIAN WELK</h1>
      <div class="brand-rule"></div>
      <p class="brand-tagline">NATUROPATHY</p>
      <p class="brand-contact">dorianwelk.com.au &nbsp; hello@dorianwelk.com.au</p>
    </header>

    <div class="leaf-decoration" role="img" aria-label="Faint overlapping skeleton leaves decoration in pale orange"></div>

    <div class="footer-band-light"></div>
    <footer class="footer">
      <span class="footer-address">Dorian Welk Naturopath · Shop 4123c, 46 Carrow Lane, Sydney 2000</span>
    </footer>
  </main>
</body>
</html>
```